Foreclosure Postcard for Consumer Attorneys

We are a law firm representing consumers in the areas of bankruptcy and foreclosure. We need a postcard to send to consumers who are already in foreclosure. We want them to know that they have options and that we can help them save their homes. They don't have to lose their homes to the bank. We're looking for designs using the colors red and white and the word "FORECLOSURE" in large print, displayed prominently on the postcard. People in this situation often throw their mail away because they get so many bills. We want this to catch their attention and for them to call us. So we also want our phone number 270-418-3297 displayed prominently.

Target Market(s)

Consumers in Foreclosure

Industry/Entity Type

Law Firm

Font styles to use
Serif
Sans Serif

Requirements
Must have
• Phone number: 270-418-3297
Darrow & Penfield, P.S.C.
248 North Maple Avenue
Bellmont, KY 42716

```html
<!DOCTYPE html>
<html lang="en">
<head>
<meta charset="utf-8">
<title>Foreclosure Postcard – Darrow &amp; Penfield, P.S.C.</title>
<link rel="stylesheet" href="https://fonts.googleapis.com/css2?family=Roboto+Slab:wght@800&family=IM+Fell+English&family=Libre+Baskerville:wght@400;700&family=Lato:wght@400&display=swap">
<style>
  :root {
    --paper: #ffffff;
    --headline-light: #f22a22;
    --headline-dark: #a30d0a;
    --headline-edge: #6a0605;
    --arrow-top: #8c8f92;
    --arrow-bottom: #ffffff;
    --ink: #1f2320;
    --firm: #3a3d34;
  }
  * { margin: 0; padding: 0; box-sizing: border-box; }
  html, body {
    width: 1200px;
    height: 924px;
    overflow: hidden;
    background: var(--paper);
  }
  .postcard {
    position: relative;
    width: 1200px;
    height: 924px;
    background: var(--paper);
    overflow: hidden;
  }
  .arrow {
    position: absolute;
    inset: 0;
  }
  .headline {
    position: absolute;
    top: 22px;
    left: -20px;
    width: 1200px;
    text-align: center;
    font-family: "Roboto Slab", serif;
    font-weight: 800;
    font-size: 148px;
    line-height: 1.1;
    letter-spacing: 3px;
    white-space: nowrap;
    background: linear-gradient(180deg, var(--headline-light) 25%, var(--headline-dark) 85%);
    -webkit-background-clip: text;
    background-clip: text;
    color: transparent;
    -webkit-text-stroke: 1px var(--headline-edge);
    filter: drop-shadow(3px 3px 2px rgba(60, 0, 0, 0.45));
  }
  .tagline {
    position: absolute;
    top: 372px;
    left: 0;
    width: 1214px;
    text-align: center;
    font-family: "IM Fell English", serif;
    font-size: 84px;
    color: var(--ink);
    letter-spacing: 2px;
    word-spacing: 8px;
    -webkit-text-stroke: 1.5px var(--ink);
  }
  .phone {
    position: absolute;
    top: 494px;
    left: 0;
    width: 1212px;
    text-align: center;
    font-family: "Libre Baskerville", serif;
    font-weight: 700;
    font-size: 78px;
    color: var(--ink);
  }
  .firm-mark {
    position: absolute;
    left: 38px;
    top: 737px;
    width: 520px;
    height: 140px;
    display: flex;
    align-items: center;
    gap: 16px;
  }
  .firm-mark .square {
    width: 140px;
    height: 140px;
    background: var(--firm);
    flex: none;
  }
  .firm-mark .name {
    font-family: "Libre Baskerville", serif;
    font-weight: 400;
    font-size: 42px;
    line-height: 1.1;
    color: var(--firm);
  }
  .address {
    position: absolute;
    right: 53px;
    top: 728px;
    font-family: "Lato", sans-serif;
    font-style: normal;
    font-size: 28px;
    line-height: 47px;
    color: var(--ink);
    letter-spacing: 0.5px;
    text-align: left;
  }
  .address .city { padding-left: 20px; }
</style>
</head>
<body>
  <main class="postcard">
    <svg class="arrow" width="1200" height="924" viewBox="0 0 1200 924" aria-hidden="true">
      <defs>
        <linearGradient id="arrow-fade" x1="0" y1="60" x2="0" y2="770" gradientUnits="userSpaceOnUse">
          <stop offset="0" stop-color="#8c8f92"/>
          <stop offset="0.55" stop-color="#c4c6c8"/>
          <stop offset="1" stop-color="#ffffff"/>
        </linearGradient>
      </defs>
      <polygon points="604,60 937,472 818,472 818,770 392,770 392,472 272,472" fill="url(#arrow-fade)"/>
    </svg>

    <h1 class="headline">FORECLOSURE</h1>
    <p class="tagline">You Have Options</p>
    <p class="phone">270-418-3297</p>

    <div class="firm-mark">
      <span class="square"></span>
      <span class="name">Darrow &amp;<br>Penfield, P.S.C.</span>
    </div>

    <address class="address">
      <div>Darrow &amp; Penfield, P.S.C.</div>
      <div>248 North Maple Avenue</div>
      <div class="city">Bellmont, KY 42716</div>
    </address>
  </main>
</body>
</html>
```